Commercial Real Estate Appraisal Company needs a postcard design

We need a postcard design for a commercial real estate company based out of Ballston Lake, New York called "Northfield Appraisers".

Northfield Appraisers, LLC., provides high quality commercial appraisal and real estate consulting services to our clients. Our company provides appraisal services for financial lending institutions, real estate developers, local municipalities, attorney’s, private individuals and businesses. Significant capital expenditures were made to ensure we can provide top of the line data research and research publications, as well as, generate our reports with industry leading appraisal software for increased accuracy and efficiency.

Services we provide

Advisory & Consulting Services, Net Lease Valuation, Capitalization Rate Consultation, Operating Expense Consultation, Discounted Cash Flow Analysis, Portfolio Valuation, Expert Witness Services, Property and Comparable Analyses, Financial Feasibility Studies, Property Tax Services, Going Concern Valuations, Real Estate Due Diligence Analyses, Highest and Best Use Studies, Real Estate Valuation, Lease Versus Purchase Analyses, Rent Arbitration and Consultation, Market Rent Analyses, Sale Lease-Backs Analysis, Market Studies, Site Inspections, Divorce Proceedings, Probate / Estate Matters

Please save room on the card for postage and addressing

Industry/Entity Type

Real Estate

```html
<!DOCTYPE html>
<html lang="en">
<head>
<meta charset="utf-8">
<title>Northfield Appraisers – Postcard</title>
<link href="https://fonts.googleapis.com/css2?family=Roboto+Condensed:wght@400;700&display=swap" rel="stylesheet">
<style>
  :root {
    --canvas: #ffffff;
    --panel: #8aa4c4;
    --band-light: #8fa8c6;
    --blue: #1e8fd8;
    --green: #1f9150;
    --slate: #4e5560;
    --cyan: #18b4e6;
    --navy: #1c2742;
    --headline: #4a5263;
    --white: #ffffff;
    --frame: #ffffff;
  }
  * { box-sizing: border-box; margin: 0; padding: 0; }
  html, body { width: 1200px; height: 1000px; overflow: hidden; background: var(--canvas); }
  body { position: relative; font-family: "Roboto Condensed", "Arial Narrow", sans-serif; }

  .postcard {
    position: absolute;
    background: var(--white);
    box-shadow: 3px 4px 6px rgba(0,0,0,0.35);
    overflow: hidden;
  }
  .postcard svg.waves { position: absolute; left: 0; top: 0; }

  /* Back side */
  .postcard--back { left: 33px; top: 33px; width: 729px; height: 517px; }
  .stamp-box {
    position: absolute; left: 597px; top: 53px; width: 89px; height: 66px;
    border: 1px solid #222; border-radius: 2px;
  }
  .brand {
    position: absolute; text-align: center; color: var(--navy);
  }
  .brand__mark { display: block; margin: 0 auto 6px; background: var(--navy); }
  .brand__name { font-weight: 700; text-transform: uppercase; letter-spacing: 0.5px; white-space: nowrap; }
  .brand__tagline { font-weight: 400; text-transform: uppercase; letter-spacing: 1px; white-space: nowrap; }

  .postcard--back .brand { left: 20px; top: 6px; width: 215px; }
  .postcard--back .brand__mark { width: 40px; height: 40px; margin-top: 4px; }
  .postcard--back .brand__name { font-size: 14px; line-height: 16px; }
  .postcard--back .brand__tagline { font-size: 7px; line-height: 9px; }

  .services { position: absolute; left: 8px; top: 156px; color: var(--white); }
  .services__title { font-size: 15px; font-weight: 700; margin-bottom: 8px; }
  .services__list { list-style: none; font-size: 11.4px; font-weight: 700; line-height: 14.45px; }

  .snapshot {
    position: absolute; border: 5px solid var(--frame);
    box-shadow: 1px 2px 4px rgba(0,0,0,0.3);
  }
  .snapshot--cottage {
    left: 194px; top: 168px; width: 152px; height: 104px; transform: rotate(14deg);
    background: linear-gradient(180deg, #8fc2ea 0%, #d8e4ea 45%, #7b8f5c 80%, #4d6a34 100%);
  }
  .snapshot--colonial {
    left: 193px; top: 330px; width: 150px; height: 98px; transform: rotate(-13deg);
    background: linear-gradient(180deg, #5f8a3c 0%, #c9d2d8 40%, #a7b0b6 65%, #4f8a30 100%);
  }

  /* Front side */
  .postcard--front { left: 411px; top: 516px; width: 747px; height: 456px; }
  .hero-photo {
    position: absolute; left: 0; top: 0; width: 747px; height: 260px;
    background: linear-gradient(180deg, #7aa6d8 0%, #4f7a3a 22%, #c7b8a0 45%, #b79f86 62%, #5d8d3a 80%, #8a7a66 100%);
  }
  .headline {
    position: absolute; left: 18px; top: 327px;
    font-size: 26px; line-height: 34px; font-weight: 700; color: var(--headline);
  }
  .headline span { display: block; }
  .headline span + span { padding-left: 6px; }
  .postcard--front .brand { left: 450px; top: 300px; width: 290px; }
  .postcard--front .brand__mark { width: 58px; height: 58px; }
  .postcard--front .brand__name { font-size: 19px; line-height: 21px; }
  .postcard--front .brand__tagline { font-size: 8.5px; line-height: 11px; }
</style>
</head>
<body>

<section class="postcard postcard--back" aria-label="Postcard back">
  <svg class="waves" width="729" height="517" viewBox="0 0 729 517" aria-hidden="true">
    <rect x="0" y="70" width="365" height="447" fill="var(--panel)"/>
    <path d="M0,0 H365 V75 C260,72 150,100 0,100 Z" fill="var(--white)"/>
    <path d="M0,100 C120,108 250,92 365,95 L365,110 C250,110 120,125 0,122 Z" fill="var(--blue)"/>
    <path d="M0,117 C150,127 260,102 365,97 V135 C260,130 150,140 0,136 Z" fill="var(--green)"/>
    <path d="M0,130 C150,142 260,135 365,135 L365,140 C260,143 150,154 0,152 Z" fill="var(--slate)"/>
    <path d="M240,150 C290,140 330,138 365,138 V162 C320,152 280,148 240,150 Z" fill="var(--cyan)"/>
  </svg>

  <div class="brand">
    <span class="brand__mark" aria-hidden="true"></span>
    <div class="brand__name">Northfield Appraisers</div>
    <div class="brand__tagline">Real Estate Appraisers &amp; Consultants</div>
  </div>

  <div class="stamp-box" aria-label="Postage area"></div>

  <div class="services">
    <h2 class="services__title">Services we provide :</h2>
    <ul class="services__list">
      <li>Advisory &amp; Consulting Services</li>
      <li>Net Lease Valuation</li>
      <li>Capitalization Rate Consultation</li>
      <li>Operating Expense Consultation</li>
      <li>Discounted Cash Flow Analysis</li>
      <li>Portfolio Valuation</li>
      <li>Expert Witness Services,</li>
      <li>Property and Comparable Analyses,</li>
      <li>Financial Feasibility Studies</li>
      <li>Property Tax Services</li>
      <li>Going Concern Valuations</li>
      <li>Real Estate Due Diligence Analyses</li>
      <li>Highest and Best Use Studies</li>
      <li>Real Estate Valuation</li>
      <li>Lease Versus Purchase Analyses</li>
      <li>Rent Arbitration and Consultation</li>
      <li>Market Rent Analyses</li>
      <li>Sale Lease-Backs Analysis</li>
      <li>Market Studies</li>
      <li>Site Inspections</li>
      <li>Divorce Proceedings</li>
      <li>Probate / Estate Matters</li>
    </ul>
  </div>

  <div class="snapshot snapshot--cottage" role="img" aria-label="Photo of a white single-storey cottage with porch under a blue sky"></div>
  <div class="snapshot snapshot--colonial" role="img" aria-label="Photo of a two-storey colonial house with green lawn"></div>
</section>

<section class="postcard postcard--front" aria-label="Postcard front">
  <div class="hero-photo" role="img" aria-label="Photo of a large stucco and stone family home with a two-car garage, driveway and landscaped garden"></div>
  <svg class="waves" width="747" height="456" viewBox="0 0 747 456" aria-hidden="true">
    <path d="M0,240 C200,250 450,200 747,205 V456 H0 Z" fill="var(--white)"/>
    <path d="M0,232 C220,238 460,196 747,200 V232 C480,228 240,250 0,250 Z" fill="var(--band-light)"/>
    <path d="M0,240 C200,250 420,238 560,236 L560,244 C400,248 200,262 0,262 Z" fill="var(--blue)"/>
    <path d="M80,258 C280,250 520,222 747,228 V272 C540,262 300,262 80,264 Z" fill="var(--green)"/>
    <path d="M0,262 C200,268 450,262 747,268 V276 C470,270 220,292 0,294 Z" fill="var(--slate)"/>
    <path d="M500,292 C600,286 680,284 747,284 V312 C680,300 580,295 500,292 Z" fill="var(--cyan)"/>
  </svg>

  <h1 class="headline">
    <span>High quality commercial appraisal</span>
    <span>&amp; Real estate consulting services</span>
  </h1>

  <div class="brand">
    <span class="brand__mark" aria-hidden="true"></span>
    <div class="brand__name">Northfield Appraisers</div>
    <div class="brand__tagline">Real Estate Appraisers &amp; Consultants</div>
  </div>
</section>

</body>
</html>
```